Website offering services oriented to the metaverse and blockchain

We need an ecommerce website theme/template for a new company named Pavreno (a play on words for BERUNDA the inventor of Vextrum). Pavreno will provide metaverse services such as:
• Pavreno Coin
• Pavreno wallet
• Pavreno Exchange
• Pavreno NFT
• Pavreno Tech
• Pavreno Pay
• Pavreno CaaS (community as a service)
• Pavreno CRM
• Pavreno Experience
• Pavreno Blockchain
• Pavreno Commerce
• Pavreno Space (as in outer space)
• Pavreno Art (sub of NFT)
• Pavreno Store

You can find our actual logo at the following link, in order to show us templates aligned with our brand:
https://files.plomvarek.com/share/folders/7kWmTzeQaLpYbNcVxRuHsJdGfOiAy2MnE?mode=view

Looking forward to heard back from you,

Designs look the same

We need a WordPress ecommerce website theme/template for a new company named Pavreno (a play on words for BERUNDA the inventor of Vextrum). Pavreno will provide metaverse services such as: • Pavreno Coin • Pavreno wallet • Pavreno Exchange • Pavreno NFT • Pavreno Tech • Pavreno Pay • Pavreno CaaS (community as a service) • Pavreno CRM • Pavreno Experience • Pavreno Blockchain • Pavreno Commerce • Pavreno Space (as in outer space) • Pavreno Art (sub of NFT) • Pavreno Store You can find our actual logo at the following link, in order to show us templates aligned with our brand: https://files.plomvarek.com/share/folders/7kWmTzeQaLpYbNcVxRuHsJdGfOiAy2MnE?mode=view Looking forward to heard back from you,

Target Market(s)

Blockchain & Cryptocurrency Businesses

Industry/Entity Type

B2C, B2B Services.

Font styles to use
Other font styles liked:
• Monserrat, Helvetica, Object Sans

Requirements
Nice to have
• Light background picture,
Should not have
• Arch designs

```html
<!DOCTYPE html>
<html lang="en">
<head>
<meta charset="utf-8">
<title>Pavreno — Metaverse &amp; Blockchain Services</title>
<link href="https://fonts.googleapis.com/css2?family=Montserrat:wght@400;500;600;700&display=swap" rel="stylesheet">
<style>
:root{
  --navy:#1d2b7a;
  --blue:#2443b8;
  --hero-a:#2a2fb0;
  --hero-b:#4b23a8;
  --feat-a:#1d6fd6;
  --feat-b:#2a2bc2;
  --ink:#222;
  --muted:#555;
  --line:#d9d9de;
  --soft:#f3f5f8;
  --footer:#141414;
  --white:#fff;
}
*{margin:0;padding:0;box-sizing:border-box}
html,body{width:1200px;height:4071px;overflow:hidden;background:var(--white)}
body{font-family:"Montserrat",Helvetica,Arial,sans-serif;color:var(--ink);position:relative}
.section{position:absolute;left:0;width:1200px}
.abs{position:absolute}
.brand{font-weight:700;letter-spacing:1px;color:var(--white)}
.heading{font-weight:600;font-size:33px;text-align:center;color:var(--ink);left:0;width:1200px}
.rule{height:3px;width:50px;background:var(--navy);left:575px}
.small{font-family:Helvetica,Arial,sans-serif;font-size:12.5px;line-height:25px;color:var(--muted)}

/* hero */
.hero{top:0;height:772px;background:linear-gradient(115deg,var(--hero-a) 0%,#2b2fb8 50%,var(--hero-b) 100%)}
.hero .brand{left:111px;top:55px;font-size:34px}
.nav{top:66px;font-size:13px;font-weight:600;color:var(--white)}
.hero-title{top:168px;left:0;width:1200px;text-align:center;font-size:47px;font-weight:700;color:var(--white);letter-spacing:1px}
.hero-sub{top:240px;left:0;width:1200px;text-align:center;font-size:18.5px;font-weight:600;color:var(--white)}
.hero-art{left:205px;top:290px;width:890px;height:360px;border-radius:8px;
  background:radial-gradient(ellipse at 20% 55%,#2f8ef0 0%,rgba(47,142,240,0) 35%),radial-gradient(ellipse at 78% 45%,#3b55e6 0%,rgba(59,85,230,0) 45%),rgba(255,255,255,.03)}

/* services */
.services{top:772px;height:635px}
.svc{width:300px;text-align:center}
.svc-art{width:200px;height:190px;margin:0 auto;border-radius:10px;background:linear-gradient(145deg,#e9ecfb,#c7cff5)}
.svc h3{font-size:20px;font-weight:500;margin-top:26px;color:var(--ink)}
.svc p{margin-top:12px}
.btn-outline{display:inline-block;margin-top:22px;width:139px;height:44px;line-height:40px;border:2px solid var(--navy);border-radius:22px;font-size:13px;font-weight:500;color:var(--navy)}

/* features */
.features{top:1407px;height:594px;background:linear-gradient(180deg,var(--feat-a) 0%,var(--feat-b) 100%)}
.features h2{left:160px;top:80px;font-size:35px;font-weight:600;color:var(--white)}
.features .rule{left:160px;top:134px;background:var(--white);width:56px}
.features .intro{left:163px;top:162px;width:400px;color:var(--white);font-family:Helvetica,Arial,sans-serif;font-size:12.5px;line-height:26px}
.checks{left:165px;top:265px;list-style:none;color:var(--white);font-family:Helvetica,Arial,sans-serif;font-size:12.5px}
.checks li{height:45px;display:flex;align-items:center;gap:26px}
.feat-art{left:585px;top:0;width:615px;height:594px;background:radial-gradient(ellipse at 55% 45%,rgba(120,190,255,.55) 0%,rgba(60,120,230,.15) 45%,rgba(0,0,0,0) 70%)}

/* faq */
.faq{top:2001px;height:584px}
.faq-list{left:191px;top:162px;width:818px;list-style:none}
.faq-list li{height:72px;border-bottom:1px solid var(--line);display:flex;align-items:center;gap:20px;font-size:19px;font-weight:500;color:var(--ink)}
.plus{width:50px;height:50px;border:1px solid #b9bfd8;border-radius:50%;display:flex;align-items:center;justify-content:center;color:var(--navy);font-size:24px;font-weight:500}

/* blog */
.blog{top:2585px;height:629px;background:var(--soft)}
.card{top:133px;width:471px;height:430px;background:var(--white);box-shadow:0 1px 4px rgba(0,0,0,.08)}
.card-img{width:471px;height:256px}
.card .date{margin:30px 0 0 32px;font-size:17px;font-weight:600;color:var(--navy)}
.card h4{margin:12px 0 0 32px;font-size:19px;font-weight:500;color:#333}
.card p{margin:10px 32px 0 32px}

/* contact */
.contact{top:3214px;height:527px;background:linear-gradient(90deg,#f4f5f7 0%,#eceef2 55%,#dfe3ea 100%)}
.contact-photo{left:720px;top:0;width:480px;height:527px;background:linear-gradient(160deg,#e7ebf1 0%,#c9d6ea 50%,#a8bde0 100%)}
.contact h2{left:111px;top:56px;font-size:35px;font-weight:600;color:#222}
.field{left:111px;width:392px;border:1px solid #6f7480;background:rgba(255,255,255,.55);font-family:Helvetica,Arial,sans-serif;font-size:13px;color:#444;padding:15px 18px}
.submit{left:111px;top:421px;width:125px;height:49px;background:var(--navy);color:var(--white);font-size:16px;font-weight:600;display:flex;align-items:center;justify-content:center}

/* footer */
.footer{top:3741px;height:330px;background:var(--footer);color:var(--white)}
.footer .brand{left:0;width:1200px;text-align:center;top:52px;font-size:38px}
.fnav{top:134px;font-size:13px;font-weight:600;transform:translateX(-50%)}
.social{top:182px;width:36px;height:36px;border:2px solid var(--white);border-radius:50%}
.copy{left:0;width:1200px;top:255px;text-align:center;font-size:15px}
</style>
</head>
<body>

<header class="section hero">
  <div class="abs brand">PAVRENO</div>
  <span class="abs nav" style="left:391px">HOME</span>
  <span class="abs nav" style="left:496px">ABOUT US</span>
  <span class="abs nav" style="left:631px">SERVICES</span>
  <span class="abs nav" style="left:762px">BENEFITS</span>
  <span class="abs nav" style="left:892px">NEWS</span>
  <span class="abs nav" style="left:997px">CONTACT US</span>
  <h1 class="abs hero-title">PAVRENO</h1>
  <p class="abs hero-sub">SED UT PERSPICIATIS UNDE OMNIS ISTE NATUS ERROR</p>
  <div class="abs hero-art" role="img" aria-label="Isometric illustration of a glowing coin connected by circuit lines to a server block"></div>
</header>

<section class="section services">
  <h2 class="abs heading" style="top:66px">OUR SERVICES</h2>
  <div class="abs rule" style="top:113px"></div>
  <div class="abs svc" style="left:120px;top:176px">
    <div class="svc-art" role="img" aria-label="Illustration of a laptop with stacked coins"></div>
    <h3>SERVICES 01</h3>
    <p class="small">Sed ut perspiciatis unde omnis iste natus<br>error sit voluptatem accusantium dolorem<br>laudantium, totam rem aperiam</p>
    <span class="btn-outline">LEARN MORE</span>
  </div>
  <div class="abs svc" style="left:450px;top:176px">
    <div class="svc-art" role="img" aria-label="Illustration of a central coin hub linked to devices"></div>
    <h3>SERVICES 02</h3>
    <p class="small">Sed ut perspiciatis unde omnis iste natus<br>error sit voluptatem accusantium dolorem<br>laudantium, totam rem aperiam</p>
    <span class="btn-outline">LEARN MORE</span>
  </div>
  <div class="abs svc" style="left:781px;top:176px">
    <div class="svc-art" role="img" aria-label="Illustration of a laptop with a secure check mark and coins"></div>
    <h3>SERVICES 03</h3>
    <p class="small">Sed ut perspiciatis unde omnis iste natus<br>error sit voluptatem accusantium dolorem<br>laudantium, totam rem aperiam</p>
    <span class="btn-outline">LEARN MORE</span>
  </div>
</section>

<section class="section features">
  <div class="abs feat-art" role="img" aria-label="Digital chain links resting on a wireframe hand"></div>
  <h2 class="abs">OUR FEATURES</h2>
  <div class="abs rule"></div>
  <p class="abs intro">Sed ut perspiciatis unde omnis iste natus error sit voluptatem acc usantium doloremque laudantium, totam rem aperiam, eaq quae ab illo inventore veritatis et quasi architecto</p>
  <ul class="abs checks">
    <li><svg width="14" height="11" viewBox="0 0 14 11"><path d="M1 5.5l4 4L13 1" fill="none" stroke="#fff" stroke-width="2.4"/></svg>Nemo enim ipsam voluptatem quia</li>
    <li><svg width="14" height="11" viewBox="0 0 14 11"><path d="M1 5.5l4 4L13 1" fill="none" stroke="#fff" stroke-width="2.4"/></svg>voluptas sit aspernatur aut odit aut fugit</li>
    <li><svg width="14" height="11" viewBox="0 0 14 11"><path d="M1 5.5l4 4L13 1" fill="none" stroke="#fff" stroke-width="2.4"/></svg>sed quia consequuntur magni dolores</li>
    <li><svg width="14" height="11" viewBox="0 0 14 11"><path d="M1 5.5l4 4L13 1" fill="none" stroke="#fff" stroke-width="2.4"/></svg>eos qui ratione voluptatem sequi nesciunt</li>
    <li><svg width="14" height="11" viewBox="0 0 14 11"><path d="M1 5.5l4 4L13 1" fill="none" stroke="#fff" stroke-width="2.4"/></svg>Neque porro quisquam est, qui dolorem</li>
    <li><svg width="14" height="11" viewBox="0 0 14 11"><path d="M1 5.5l4 4L13 1" fill="none" stroke="#fff" stroke-width="2.4"/></svg>ipsum quia dolor sit amet, consectetur</li>
  </ul>
</section>

<section class="section faq">
  <h2 class="abs heading" style="top:48px">OUR FAQ’S</h2>
  <div class="abs rule" style="top:101px"></div>
  <ul class="abs faq-list">
    <li><span class="plus">+</span>Sed ut perspiciatis unde omnis iste natus error?</li>
    <li><span class="plus">+</span>Nemo enim ipsam voluptatem quia voluptas sit?</li>
    <li><span class="plus">+</span>Sed ut perspiciatis unde natus error?</li>
    <li><span class="plus">+</span>Nemo enim ipsam voluptatem quia voluptas sit?</li>
    <li><span class="plus">+</span>Sed ut perspiciatis unde natus error?</li>
  </ul>
</section>

<section class="section blog">
  <h2 class="abs heading" style="top:47px">LATEST BLOG</h2>
  <div class="abs rule" style="top:99px"></div>
  <article class="abs card" style="left:111px">
    <div class="card-img" role="img" aria-label="Photo of hands typing on a laptop with network lock icons" style="background:linear-gradient(120deg,#2c3e63,#1a2a4a 55%,#4a3a34)"></div>
    <div class="date">23 DEC 2021</div>
    <h4>Sed ut perspiciatis unde omnis</h4>
    <p class="small">Nemo enim ipsam voluptatem quia voluptas sit aspernatur aut odit aut fugit, sed quia consequuntur magni dolores</p>
  </article>
  <article class="abs card" style="left:617px">
    <div class="card-img" role="img" aria-label="Digital illustration of two glowing hands shaking" style="background:linear-gradient(120deg,#0b1548,#123a7a 50%,#0b1548)"></div>
    <div class="date">23 DEC 2021</div>
    <h4>Sed ut perspiciatis unde omnis</h4>
    <p class="small">Nemo enim ipsam voluptatem quia voluptas sit aspernatur aut odit aut fugit, sed quia consequuntur magni dolores</p>
  </article>
</section>

<section class="section contact">
  <div class="abs contact-photo" role="img" aria-label="Photo of a smiling man working on a laptop in a bright office"></div>
  <h2 class="abs">CONTACT US</h2>
  <div class="abs field" style="top:135px;height:49px">Name :</div>
  <div class="abs field" style="top:196px;height:49px">Email :</div>
  <div class="abs field" style="top:258px;height:49px">Phone :</div>
  <div class="abs field" style="top:320px;height:82px">Message :</div>
  <div class="abs submit">SUBMIT</div>
</section>

<footer class="section footer">
  <div class="abs brand">PAVRENO</div>
  <span class="abs fnav" style="left:285px">HOME</span>
  <span class="abs fnav" style="left:400px">ABOUT US</span>
  <span class="abs fnav" style="left:527px">SERVICES</span>
  <span class="abs fnav" style="left:653px">BENEFITS</span>
  <span class="abs fnav" style="left:765px">NEWS</span>
  <span class="abs fnav" style="left:889px">CONTACT US</span>
  <span class="abs social" style="left:537px" aria-label="Social link"></span>
  <span class="abs social" style="left:580px" aria-label="Social link"></span>
  <span class="abs social" style="left:624px" aria-label="Social link"></span>
  <p class="abs copy">© Copyright 2021 Pavreno.All Rights Reserved.</p>
</footer>

</body>
</html>
```